Skip Bin Hire Business

We are an existing business that hire out skip bins for domestic and commercial use. We are looking for a fresh look with no colours or designs in mind.
We have 2m3 and 3m3 skip bins and 3m3 up to 24m3 walk in bins.
Visit our website for more information.
www.harborcrate.com.au
We are going to add a photo of a 3m3 skip as this is a new product for our company and not available on our website at this stage.

Industry/Entity Type

Business

Contact Information for Business Card

Harbor Crate
9172-4086
www.harborcrate.com.au

```html
<!DOCTYPE html>
<html lang="en">
<head>
<meta charset="UTF-8">
<title>Harbor Crate – Business Card</title>
<link rel="stylesheet" href="https://fonts.googleapis.com/css2?family=Mulish:wght@600;700;800;900&display=swap">
<style>
  :root {
    --backdrop: #3a2d29;
    --card-white: #ffffff;
    --mustard: #c8920f;
    --photo-light: #e3b42a;
    --photo-dark: #c99a14;
    --ink: #1d1d1d;
    --ink-soft: #333333;
    --on-band: #ffffff;
  }

  * { box-sizing: border-box; margin: 0; padding: 0; }

  html, body {
    width: 1200px;
    height: 450px;
    overflow: hidden;
  }

  body {
    background: var(--backdrop);
    font-family: "Mulish", "Century Gothic", sans-serif;
    display: flex;
    align-items: center;
    justify-content: center;
  }

  .business-card {
    position: relative;
    width: 680px;
    height: 390px;
    background: var(--card-white);
    box-shadow: 0 10px 28px rgba(0, 0, 0, 0.45);
    overflow: hidden;
  }

  .product-photo {
    position: absolute;
    left: 36px;
    top: 22px;
    width: 210px;
    height: 134px;
    background: linear-gradient(180deg, var(--photo-light) 0%, var(--photo-dark) 100%);
  }

  .brand-name {
    position: absolute;
    right: 48px;
    top: 26px;
    text-align: right;
    font-weight: 900;
    font-size: 48px;
    line-height: 0.92;
    letter-spacing: -0.5px;
    color: var(--ink-soft);
    text-transform: uppercase;
  }

  .tagline {
    position: absolute;
    left: 36px;
    top: 170px;
    display: flex;
    align-items: center;
    gap: 10px;
    font-weight: 700;
    font-size: 15px;
    color: var(--ink);
  }

  .tagline-dot {
    width: 13px;
    height: 13px;
    border-radius: 50%;
    background: var(--mustard);
  }

  .contact-band {
    position: absolute;
    left: 0;
    top: 198px;
    width: 100%;
    height: 144px;
    background: var(--mustard);
    color: var(--on-band);
    padding: 24px 0 0 66px;
    font-weight: 800;
  }

  .contact-line {
    font-size: 31px;
    line-height: 1.45;
    letter-spacing: 0.3px;
  }

  .quote-strip {
    position: absolute;
    left: 0;
    top: 342px;
    width: 100%;
    height: 48px;
    display: flex;
    align-items: center;
    padding-left: 48px;
    font-weight: 800;
    font-size: 15px;
    color: var(--ink);
  }
</style>
</head>
<body>
  <article class="business-card">
    <div class="product-photo" role="img" aria-label="Photo of a yellow 3m³ skip bin"></div>

    <div class="brand-name">Harbor<br>Crate</div>

    <p class="tagline">
      <span>100% Australian Owned</span>
      <span class="tagline-dot"></span>
      <span>Service-focused</span>
      <span class="tagline-dot"></span>
      <span>Environmentally aware</span>
    </p>

    <section class="contact-band">
      <p class="contact-line">Harbor Crate 9172-4086</p>
      <p class="contact-line">www.harborcrate.com.au</p>
    </section>

    <p class="quote-strip">Email us to get a free quote now at admin@harborcrateaccess.com</p>
  </article>
</body>
</html>
```